quiet orchard

It is a small business that is looking to sell medical supplies and services. later down the line it will branch off to help solve other world problems, i.e. global warming and raw material shortages.
but we will start with hospital equipment and supplies.

Target Market(s)

all medical facilities

Coding

Coded - Design and coding required

Number of Pages Required

1 page

```html
<!DOCTYPE html>
<html lang="en">
<head>
<meta charset="utf-8">
<title>Quiet Orchard — Medical Supplies &amp; Services</title>
<link href="https://fonts.googleapis.com/css2?family=Roboto:wght@400;500;700&family=Montserrat:wght@400;500&display=swap" rel="stylesheet">
<style>
:root{
  --navy:#1f4b8e;
  --navy-deep:#1b447f;
  --orange:#f0923a;
  --text:#6a6a6a;
  --ink:#2b2b2b;
  --pale:#eef3f9;
  --line:#dfe4ea;
  --white:#ffffff;
}
*{margin:0;padding:0;box-sizing:border-box}
html,body{width:1200px;height:3906px;overflow:hidden}
body{position:relative;background:var(--white);font-family:'Montserrat',sans-serif;color:var(--text)}
.abs{position:absolute}
.heading{font-family:'Roboto',sans-serif;font-weight:700;color:var(--navy);text-transform:uppercase;line-height:1.22}
.eyebrow{font-family:'Roboto',sans-serif;font-size:17px;color:#333;text-transform:uppercase}
.center{text-align:center;left:0;width:1200px}
.btn{display:flex;align-items:center;justify-content:center;background:var(--orange);color:var(--white);font-family:'Roboto',sans-serif;font-weight:500;font-size:18px;border-radius:30px;text-transform:uppercase}
.para{font-size:16px;line-height:27.5px}

/* hero */
.hero{left:0;top:0;width:1200px;height:687px;background:linear-gradient(100deg,#3c6a78 0%,#2f6a84 35%,#1f5e98 65%,#15458e 100%)}
.hero-shade{left:0;top:0;width:1200px;height:687px;background:linear-gradient(90deg,rgba(20,40,60,.35),rgba(20,40,60,0) 60%)}
.logo{display:flex;align-items:center;gap:12px;font-family:'Roboto',sans-serif;color:var(--white)}
.logo .mark{width:18px;height:18px;border-radius:50%;background:var(--white);display:block}
.logo .name{font-size:26px;font-weight:500;letter-spacing:.2px}
.contact-bar{right:111px;top:20px;font-family:'Roboto',sans-serif;font-size:16px;color:var(--white);display:flex;gap:8px;align-items:center}
.nav{right:111px;top:61px;display:flex;gap:26px;font-family:'Roboto',sans-serif;font-weight:500;font-size:16px;color:var(--white)}
.nav .active{color:var(--orange)}
.hero-title{left:108px;top:238px;font-size:51px;color:var(--white)}
.dots{left:565px;top:599px;display:flex;gap:4px}
.dots span{width:14px;height:14px;border-radius:50%;border:2px solid var(--white)}
.dots span.on{background:var(--white)}

/* services */
.band{left:0;width:1200px;background:var(--pale)}
.svc-card{width:218px;height:194px;background:var(--white);border:1px solid var(--line);border-radius:8px;padding:22px 18px}
.svc-card.hl{border:2px solid var(--orange)}
.svc-card svg{display:block;height:76px}
.svc-card p{margin-top:14px;font-family:'Roboto',sans-serif;font-size:20px;color:var(--ink);line-height:25px}

/* products */
.prod{width:235px}
.prod .ph{height:289px}
.prod p{margin-top:22px;text-align:center;font-family:'Roboto',sans-serif;font-size:21px;color:var(--ink);line-height:26px}
.arrow{width:20px;height:30px}

/* news */
.news{width:311px;height:451px;background:var(--white);border:1px solid var(--line);border-radius:6px;overflow:hidden}
.news.hl{border:2px solid #e9b58a}
.news .ph{height:220px}
.news .body{padding:20px 23px}
.news h3{font-family:'Roboto',sans-serif;font-weight:400;font-size:21px;color:var(--ink)}
.news .meta{margin-top:8px;font-size:15px;color:#777;display:flex;align-items:center;gap:6px}
.news .meta svg{width:13px;height:13px}
.news .excerpt{margin-top:14px;font-size:15.5px;line-height:26px}
.news .more{margin-top:16px;font-family:'Roboto',sans-serif;font-weight:500;font-size:17px;color:var(--orange)}

/* suppliers */
.sup{width:182px;height:90px;border:1px solid var(--line);display:flex;align-items:center;justify-content:center;gap:8px;font-family:'Roboto',sans-serif;font-size:22px;font-weight:500;color:#9a9a9a;background:var(--white)}
.sup.hl{border:2px solid #e9b58a;color:var(--navy)}
.sup i{width:14px;height:14px;background:#b9b9b9;display:block}
.sup.hl i{background:var(--navy)}

/* footer */
.footer{left:0;top:3494px;width:1200px;height:412px;background:var(--navy-deep);color:var(--white)}
.footer h4{font-family:'Roboto',sans-serif;font-weight:500;font-size:19px;color:var(--white)}
.links{list-style:none;font-size:16px;line-height:28.5px;color:var(--white)}
.finfo{font-size:16px;line-height:32px;color:var(--white)}
.finfo .row{display:flex;gap:10px;align-items:flex-start}
.rule{left:111px;top:321px;width:977px;height:1px;background:rgba(255,255,255,.3)}
.copy{left:111px;top:352px;font-size:15.5px;color:var(--white)}
.social{width:42px;height:42px;border:2px solid var(--white);border-radius:50%}
</style>
</head>
<body>

<!-- hero -->
<section class="abs hero" role="img" aria-label="Gloved hand holding a syringe drawing from a medicine vial"></section>
<div class="abs hero-shade"></div>

<div class="abs logo" style="left:111px;top:38px">
  <span class="mark"></span>
  <span class="name">QUIET ORCHARD</span>
</div>

<div class="abs contact-bar">
  <svg width="14" height="14" viewBox="0 0 24 24"><path d="M6 2l4 4-2 3c1 3 3 5 6 6l3-2 4 4-3 4C10 21 3 14 2 5z" fill="#f0923a"/></svg>
  <span>1 555 010 2024</span><span>|</span>
  <svg width="16" height="12" viewBox="0 0 16 12"><rect width="16" height="12" rx="1" fill="#f0923a"/><path d="M1 1l7 6 7-6" stroke="#fff" fill="none"/></svg>
  <span>info@quietorchard.com</span>
</div>

<nav class="abs nav">
  <span class="active">HOME</span><span>ABOUT</span><span>SERVICES</span><span>PRODUCTS</span><span>NEWS</span><span>SUPPLIERS</span><span>CONTACT</span>
</nav>

<h1 class="abs heading hero-title" style="color:#fff;line-height:64px">Medical Supplies<br>&amp; Services</h1>
<div class="abs btn" style="left:111px;top:402px;width:245px;height:64px;font-size:19px">Explore Products</div>
<div class="abs dots"><span class="on"></span><span></span><span></span><span></span></div>

<!-- about -->
<p class="abs eyebrow" style="left:111px;top:756px">About us</p>
<h2 class="abs heading" style="left:111px;top:790px;font-size:36px;line-height:44px">Welcome to<br>Quiet Orchard</h2>
<p class="abs para" style="left:111px;top:902px;width:495px">Nemo enim ipsam voluptatem quia voluptas sit aspernatur aut odit aut fugit, sed quia consequuntur magni dolores eos qui ratione voluptatem sequi nesciunt. Neque porro qiluisq uam est, qui dolorem ipsum quia dolor sit amet, consec tur, adipisci velit, sed quia non numquam eius modi tempora incidunt ut labore et dolore magnam aliquam quaerat vod quia consequuntluptatem.</p>
<div class="abs btn" style="left:111px;top:1127px;width:156px;height:56px">Read more</div>
<div class="abs" role="img" aria-label="Warehouse worker in hairnet and gloves checking boxes with a tablet" style="left:658px;top:754px;width:430px;height:403px;border-radius:60px 0 0 0;background:linear-gradient(135deg,#c89a6a 0%,#d9c4a8 45%,#e6edf5 70%,#9fb9d8 100%)"></div>

<!-- services -->
<section class="abs band" style="top:1256px;height:570px"></section>

<div class="abs svc-card hl" style="left:111px;top:1323px">
  <svg viewBox="0 0 80 76" width="80"><path d="M22 34a18 18 0 0136 0" fill="none" stroke="#f0923a" stroke-width="3"/><circle cx="40" cy="32" r="13" fill="none" stroke="#f0923a" stroke-width="3"/><path d="M6 72c2-14 16-20 34-20s32 6 34 20z" fill="none" stroke="#f0923a" stroke-width="3"/><rect x="18" y="32" width="7" height="12" rx="2" fill="#f0923a"/><rect x="55" y="32" width="7" height="12" rx="2" fill="#f0923a"/></svg>
  <p>Industry specific consultancy</p>
</div>
<div class="abs svc-card" style="left:352px;top:1323px">
  <svg viewBox="0 0 80 76" width="80"><g fill="none" stroke="#1f4b8e" stroke-width="3"><rect x="8" y="18" width="14" height="54" rx="3"/><rect x="30" y="10" width="14" height="62" rx="3"/><path d="M52 4h14M59 4v14M54 18h10v46l-5 8-5-8z"/></g><g stroke="#f0923a" stroke-width="3"><path d="M11 40h8M11 50h8M33 32h8M33 44h8"/></g></svg>
  <p>Medical Equipment Supplies</p>
</div>
<div class="abs svc-card" style="left:111px;top:1547px">
  <svg viewBox="0 0 80 76" width="80"><g fill="none" stroke="#1f4b8e" stroke-width="3"><rect x="10" y="4" width="46" height="62" rx="2"/><path d="M18 16h30M18 26h30M18 36h22M18 50l6-4 6 4 6-4"/></g><circle cx="54" cy="56" r="9" fill="none" stroke="#f0923a" stroke-width="3"/><path d="M49 64l-2 10 7-4 7 4-2-10" fill="none" stroke="#f0923a" stroke-width="3"/></svg>
  <p>Sales Service &amp; Contract</p>
</div>
<div class="abs svc-card" style="left:352px;top:1547px">
  <svg viewBox="0 0 80 76" width="80"><path d="M28 28l12-7 12 7v14l-12 7-12-7z M28 28l12 7 12-7 M40 35v14" fill="none" stroke="#1f4b8e" stroke-width="3"/><g stroke="#1f4b8e" stroke-width="2.5" fill="none"><path d="M40 2v12M36 6l4-4 4 4M40 62v12M36 70l4 4 4-4M2 38h14M6 34l-4 4 4 4M64 38h14M74 34l4 4-4 4"/></g><g stroke="#f0923a" stroke-width="2.5" stroke-dasharray="3 3"><path d="M12 12l12 12M68 12L56 24M12 64l12-12M68 64L56 52"/></g></svg>
  <p>Distributing high quality products</p>
</div>

<p class="abs eyebrow" style="left:642px;top:1323px">Services</p>
<h2 class="abs heading" style="left:642px;top:1356px;font-size:36px;line-height:44px;width:520px">Providing comprehensive and custom-designed services</h2>
<p class="abs para" style="left:642px;top:1504px;width:450px">Nemo enim ipsam voluptatem quia voluptas sit asper natur aut odit aut fugit, sed quia consequuntur magni dolores eos qui ratione voluptatem sequi nesciunt ue porro qiluisq uam est, qui dolorem ipsum quia dolor st amet, consec tur, adipisci velit, sed quia non numuam eius modi tempora incidunt.</p>
<div class="abs btn" style="left:642px;top:1695px;width:156px;height:57px">Read more</div>

<!-- products -->
<p class="abs eyebrow center" style="top:1894px">Featured</p>
<h2 class="abs heading center" style="top:1930px;font-size:36px">Our Products</h2>
<svg class="abs arrow" style="left:64px;top:2143px" viewBox="0 0 20 30"><path d="M15 3L4 15l11 12" fill="none" stroke="#555" stroke-width="3"/></svg>
<svg class="abs arrow" style="left:1116px;top:2143px" viewBox="0 0 20 30"><path d="M5 3l11 12L5 27" fill="none" stroke="#555" stroke-width="3"/></svg>

<div class="abs prod" style="left:111px;top:2012px">
  <div class="ph" role="img" aria-label="Hospital patient monitors and ventilator equipment" style="background:linear-gradient(160deg,#dfe7ef,#9fb2c4 60%,#55697d)"></div>
  <p>Medical<br>Equipments</p>
</div>
<div class="abs prod" style="left:359px;top:2012px">
  <div class="ph" role="img" aria-label="Coiled infusion tubing with a blue butterfly needle" style="background:linear-gradient(150deg,#0f4c9a,#3b8fd6 55%,#b9d8f0)"></div>
  <p>Disposables &amp;<br>solutions</p>
</div>
<div class="abs prod" style="left:606px;top:2012px">
  <div class="ph" role="img" aria-label="Turquoise and white pills spilling from an amber bottle" style="background:linear-gradient(160deg,#2e2a28,#8a5a2c 35%,#4bb6c6 70%,#e8f4f6)"></div>
  <p>Pharmaceutical</p>
</div>
<div class="abs prod" style="left:854px;top:2012px">
  <div class="ph" role="img" aria-label="Gloved hands holding a rack of blood sample tubes" style="background:linear-gradient(160deg,#e9eef3,#a9c6e6 50%,#3a78c4)"></div>
  <p>Diagnostics &amp;<br>Labs</p>
</div>

<!-- news -->
<section class="abs band" style="top:2442px;height:688px"></section>
<p class="abs eyebrow center" style="top:2508px">Latest post</p>
<h2 class="abs heading center" style="top:2544px;font-size:36px">In the news</h2>

<article class="abs news" style="left:111px;top:2611px">
  <div class="ph" role="img" aria-label="Worker in white coat checking stock in a supply warehouse" style="background:linear-gradient(160deg,#e4e6ea,#c9b79c 60%,#b08a60)"></div>
  <div class="body">
    <h3>Nemo enim ipsam voluptat</h3>
    <div class="meta"><svg viewBox="0 0 13 13"><rect x="1" y="2" width="11" height="10" fill="#777"/></svg>19/01/2022 &nbsp;|&nbsp; <svg viewBox="0 0 13 13"><circle cx="6.5" cy="4" r="3" fill="#1f4b8e"/><path d="M1 13a5.5 5 0 0111 0z" fill="#1f4b8e"/></svg>Admin</div>
    <p class="excerpt">Neque porro quisquam est, qui dolorem ipsum quia dolor site consect adipisci veli.</p>
    <p class="more">READ MORE</p>
  </div>
</article>
<article class="abs news hl" style="left:444px;top:2611px">
  <div class="ph" role="img" aria-label="Surgeon in scrubs adjusting a monitor in an operating room" style="background:linear-gradient(160deg,#1d3c6a,#3f7fb8 55%,#a5cde8)"></div>
  <div class="body">
    <h3>Nemo enim ipsam voluptat</h3>
    <div class="meta"><svg viewBox="0 0 13 13"><rect x="1" y="2" width="11" height="10" fill="#777"/></svg>19/01/2022 &nbsp;|&nbsp; <svg viewBox="0 0 13 13"><circle cx="6.5" cy="4" r="3" fill="#1f4b8e"/><path d="M1 13a5.5 5 0 0111 0z" fill="#1f4b8e"/></svg>Admin</div>
    <p class="excerpt">Neque porro quisquam est, qui dolorem ipsum quia dolor site consect adipisci veli.</p>
    <p class="more">READ MORE</p>
  </div>
</article>
<article class="abs news" style="left:777px;top:2611px">
  <div class="ph" role="img" aria-label="Technician in hairnet working at a production line" style="background:linear-gradient(160deg,#eef1f4,#b9c4cf 55%,#6f7f8e)"></div>
  <div class="body">
    <h3>Nemo enim ipsam voluptat</h3>
    <div class="meta"><svg viewBox="0 0 13 13"><rect x="1" y="2" width="11" height="10" fill="#777"/></svg>19/01/2022 &nbsp;|&nbsp; <svg viewBox="0 0 13 13"><circle cx="6.5" cy="4" r="3" fill="#1f4b8e"/><path d="M1 13a5.5 5 0 0111 0z" fill="#1f4b8e"/></svg>Admin</div>
    <p class="excerpt">Neque porro quisquam est, qui dolorem ipsum quia dolor site consect adipisci veli.</p>
    <p class="more">READ MORE</p>
  </div>
</article>

<!-- suppliers -->
<p class="abs eyebrow center" style="top:3198px">Distributors</p>
<h2 class="abs heading center" style="top:3234px;font-size:36px">Suppliers</h2>
<svg class="abs arrow" style="left:67px;top:3340px" viewBox="0 0 20 30"><path d="M15 3L4 15l11 12" fill="none" stroke="#aaa" stroke-width="3"/></svg>
<svg class="abs arrow" style="left:1113px;top:3340px" viewBox="0 0 20 30"><path d="M5 3l11 12L5 27" fill="none" stroke="#aaa" stroke-width="3"/></svg>
<div class="abs sup" style="left:111px;top:3310px"><i></i>Boxwell</div>
<div class="abs sup" style="left:310px;top:3310px"><i></i>Fernlane</div>
<div class="abs sup hl" style="left:509px;top:3310px"><i></i>Swiftpath</div>
<div class="abs sup" style="left:707px;top:3310px"><i></i>Ironbrook</div>
<div class="abs sup" style="left:906px;top:3310px"><i></i>Halcyon</div>

<!-- footer -->
<footer class="abs footer">
  <div class="abs logo" style="left:111px;top:78px">
    <span class="mark" style="width:22px;height:22px"></span>
    <span class="name" style="font-size:30px">QUIET ORCHARD</span>
  </div>

  <div class="abs" style="left:500px;top:56px">
    <h4>Quick Links</h4>
    <ul class="links" style="margin-top:12px">
      <li>Home</li><li>About</li><li>Services</li><li>Products</li><li>News</li><li>Suppliers</li><li>Contact</li>
    </ul>
  </div>

  <div class="abs finfo" style="left:714px;top:56px;width:340px">
    <h4>Contact Information</h4>
    <div class="row" style="margin-top:8px"><svg width="12" height="16" viewBox="0 0 12 16" style="margin-top:8px;flex:none"><path d="M6 0a6 6 0 016 6c0 4-6 10-6 10S0 10 0 6a6 6 0 016-6z" fill="#f0923a"/><circle cx="6" cy="6" r="2" fill="#1b447f"/></svg><span>4410 Elm Grove Road<br>laudantium, totam rem ape</span></div>
    <div class="row" style="margin-top:32px"><svg width="14" height="14" viewBox="0 0 24 24" style="margin-top:9px;flex:none"><path d="M6 2l4 4-2 3c1 3 3 5 6 6l3-2 4 4-3 4C10 21 3 14 2 5z" fill="#f0923a"/></svg><span>1 555 010 2024</span></div>
    <div class="row" style="margin-top:32px"><svg width="16" height="12" viewBox="0 0 16 12" style="margin-top:10px;flex:none"><rect width="16" height="12" rx="1" fill="#f0923a"/><path d="M1 1l7 6 7-6" stroke="#1b447f" fill="none"/></svg><span>info@quietorchard.com</span></div>
  </div>

  <div class="abs rule"></div>
  <p class="abs copy">© 2021, Quiet Orchard. All Rights Reserved.</p>
  <div class="abs social" style="left:941px;top:341px" aria-label="Social profile one"></div>
  <div class="abs social" style="left:992px;top:341px" aria-label="Social profile two"></div>
  <div class="abs social" style="left:1044px;top:341px" aria-label="Social profile three"></div>
</footer>

</body>
</html>
```